Grab Fresh Prospects

I would like 4 different size banner ads. The "Standard" online sizes. I believe they are: 125x125 | 728x90 | 468x60 | 250x250 These banners will be for promoting the website. I want to make sure you can read what the banners say so NO real fancy text. I've uploaded a few ideas as I do want them to kinda look like the website. https://www.grabfreshprospects.com/ Take a look at the site and you will see we use money bags, dollar signs and bright colors.

```html
<!DOCTYPE html>
<html lang="en">
<head>
<meta charset="utf-8">
<title>Grab Fresh Prospects – Banner Set</title>
<link rel="stylesheet" href="https://fonts.googleapis.com/css2?family=Almendra+SC&family=Kaushan+Script&family=Oswald:wght@400;500&display=swap">
<style>
  :root {
    --stage: #4a2a17;
    --paper: #ffffff;
    --olive: #979b37;
    --blue-light: #27b3e6;
    --blue-deep: #1560b8;
    --income-blue: #1e86c9;
    --red: #e3232a;
    --ink: #111111;
    --label: #f3e9dc;
    --gold: #e9b93c;
    --bag-light: #e6cfa4;
    --bag-dark: #4f7a35;
  }
  * { margin: 0; padding: 0; box-sizing: border-box; }
  html, body { width: 1200px; height: 455px; overflow: hidden; }
  body { background: var(--stage); position: relative; font-family: "Oswald", sans-serif; }

  .banner { position: absolute; background: var(--paper); overflow: hidden; }
  .size-label {
    position: absolute; color: var(--label); font-family: "Oswald", sans-serif;
    font-size: 14px; letter-spacing: .5px; transform: translateX(-50%);
  }

  .headline {
    position: absolute; font-family: "Almendra SC", serif; line-height: 1;
    background: linear-gradient(180deg, var(--blue-light), var(--blue-deep));
    -webkit-background-clip: text; background-clip: text; color: transparent;
    white-space: nowrap;
  }
  .tagline-script {
    position: absolute; font-family: "Kaushan Script", cursive; color: var(--red);
    white-space: nowrap; line-height: 1;
  }
  .tagline-plain {
    position: absolute; color: var(--ink); font-family: "Oswald", sans-serif;
    text-align: center; line-height: 1.15; font-weight: 400;
  }
  .unlimited {
    position: absolute; font-family: "Almendra SC", serif; white-space: nowrap; line-height: 1;
  }
  .ongoing {
    position: absolute; font-family: "Oswald", sans-serif; white-space: nowrap; line-height: 1;
  }
  .pointer-hand {
    position: absolute; background: var(--gold); border-radius: 40% 50% 45% 40%;
  }
  .money-bag {
    position: absolute; border-radius: 45% 45% 40% 40%;
    background: linear-gradient(135deg, var(--bag-light) 0%, var(--bag-light) 45%, var(--gold) 55%, var(--bag-dark) 100%);
  }
  .olive-band { position: absolute; left: 0; right: 0; bottom: 0; background: var(--olive); }
  .divider { position: absolute; }

  /* 125 x 125 */
  .banner--square-small { left: 43px; top: 64px; width: 145px; height: 145px; }
  .banner--square-small .olive-band { height: 62px; }

  /* 468 x 60 */
  .banner--leaderboard-small { left: 266px; top: 95px; width: 538px; height: 71px; }

  /* 728 x 90 */
  .banner--leaderboard { left: 29px; top: 258px; width: 865px; height: 105px; }

  /* 250 x 250 */
  .banner--square-large { left: 882px; top: 73px; width: 289px; height: 288px; background: var(--olive); }
  .banner--square-large .top-panel { position: absolute; left: 0; top: 0; }
</style>
</head>
<body>

<!-- 125 x 125 -->
<section class="banner banner--square-small" aria-label="125 by 125 banner">
  <div class="olive-band"></div>
  <div class="headline" style="left:5px; top:5px; font-size:19px;">Grab Fresh<br>Prospects</div>
  <div class="pointer-hand" role="img" aria-label="Pointing hand illustration" style="left:116px; top:6px; width:24px; height:16px;"></div>
  <div class="tagline-plain" style="left:4px; width:137px; top:47px; font-size:11px;">Plus, A Monthly Residual<br>Income!</div>
  <div class="unlimited" style="left:8px; top:89px; font-size:15px; color:var(--paper);">Truly Unlimited</div>
  <div class="money-bag" role="img" aria-label="Money bags with coins illustration" style="left:5px; top:110px; width:32px; height:28px;"></div>
  <div class="ongoing" style="left:41px; top:116px; font-size:13px; color:var(--paper);">ONGOING INCOME!</div>
</section>
<div class="size-label" style="left:112px; top:223px;">125x125</div>

<!-- 468 x 60 -->
<section class="banner banner--leaderboard-small" aria-label="468 by 60 banner">
  <div class="pointer-hand" role="img" aria-label="Pointing hand illustration" style="left:6px; top:9px; width:30px; height:16px;"></div>
  <div class="headline" style="left:40px; top:5px; font-size:23px;">Grab Fresh Prospects</div>
  <div class="tagline-script" style="left:8px; top:37px; font-size:16px;">Plus, A Monthly Residual Income!</div>
  <svg class="divider" style="left:302px; top:0;" width="22" height="71" viewBox="0 0 22 71" aria-hidden="true">
    <polyline points="4,2 18,35.5 4,69" fill="none" stroke="var(--olive)" stroke-width="4"/>
  </svg>
  <div class="unlimited" style="left:340px; top:7px; font-size:20px; color:var(--red);">Truly Unlimited</div>
  <div class="money-bag" role="img" aria-label="Money bags with coins illustration" style="left:328px; top:31px; width:50px; height:36px;"></div>
  <div class="ongoing" style="left:383px; top:37px; font-size:18px; color:var(--income-blue);">ONGOING INCOME!</div>
</section>
<div class="size-label" style="left:553px; top:182px;">468x60</div>

<!-- 728 x 90 -->
<section class="banner banner--leaderboard" aria-label="728 by 90 banner">
  <div class="pointer-hand" role="img" aria-label="Pointing hand illustration" style="left:8px; top:14px; width:46px; height:26px;"></div>
  <div class="headline" style="left:60px; top:8px; font-size:37px;">Grab Fresh Prospects</div>
  <div class="tagline-script" style="left:8px; top:54px; font-size:26px;">Plus, A Monthly Residual Income!</div>
  <svg class="divider" style="left:482px; top:0;" width="30" height="105" viewBox="0 0 30 105" aria-hidden="true">
    <polyline points="5,3 24,52.5 5,102" fill="none" stroke="var(--olive)" stroke-width="5"/>
  </svg>
  <div class="unlimited" style="left:525px; top:10px; font-size:30px; color:var(--red);">Truly Unlimited</div>
  <div class="money-bag" role="img" aria-label="Money bags with coins illustration" style="left:520px; top:42px; width:78px; height:56px;"></div>
  <div class="ongoing" style="left:607px; top:48px; font-size:31px; color:var(--income-blue);">ONGOING INCOME!</div>
</section>
<div class="size-label" style="left:342px; top:373px;">728x90</div>

<!-- 250 x 250 -->
<section class="banner banner--square-large" aria-label="250 by 250 banner">
  <svg class="top-panel" width="289" height="176" viewBox="0 0 289 176" aria-hidden="true">
    <polygon points="0,0 289,0 289,155 144.5,174 0,155" fill="var(--paper)"/>
  </svg>
  <div class="headline" style="left:8px; top:14px; font-size:37px; line-height:1.1;">Grab Fresh<br>Prospects</div>
  <div class="pointer-hand" role="img" aria-label="Pointing hand illustration" style="left:248px; top:8px; width:34px; height:34px;"></div>
  <div class="tagline-plain" style="left:6px; width:277px; top:96px; font-size:22px;">Plus, A Monthly Residual<br>Income!</div>
  <div class="unlimited" style="left:14px; top:185px; font-size:27px; color:var(--paper);">Truly Unlimited</div>
  <div class="money-bag" role="img" aria-label="Money bags with coins illustration" style="left:10px; top:218px; width:62px; height:58px;"></div>
  <div class="ongoing" style="left:78px; top:233px; font-size:25px; color:var(--paper);">ONGOING INCOME!</div>
</section>
<div class="size-label" style="left:1024px; top:370px;">250x250</div>

</body>
</html>
```